Street Light Box

We need a New Illuminated light Box Sign. See size in attached document and pics of current sign.
The light box needs to contain "The Harborvale Motel"and then in one third of the box at the bottom promote the restaurant on site. I want white text on black without the logo. Harborvale to be prominent word with elongated text to maximise text size for maximum visibility from a distance.

Target Market(s)

Catch attention of motel

Industry/Entity Type

Motel accommodation

Logo Text

The Harborvale Motel and below Mirokawa Robatayaki Restaurant

Logo styles of interest
Wordmark Logo
Lettermark Logo
Font styles to use
Sans Serif

Colors

Designer to choose only greyscale colors for use in the design.

Requirements
Must have
• Fit in Light Box
Nice to have
• Make Harborvale the Champion work with Elongated thick Text

```html
<!DOCTYPE html>
<html lang="en">
<head>
<meta charset="utf-8">
<title>The Harborvale Motel – Light Box Sign</title>
<link rel="stylesheet" href="https://fonts.googleapis.com/css2?family=Bebas+Neue&display=swap">
<style>
  :root {
    --backdrop: #e6e6e6;
    --sign-black: #000000;
    --sign-white: #ffffff;
  }
  html, body {
    margin: 0;
    padding: 0;
    width: 1198px;
    height: 1200px;
    overflow: hidden;
    background: var(--backdrop);
  }
  .canvas {
    position: relative;
    width: 1198px;
    height: 1200px;
  }
  .light-box {
    position: absolute;
    left: 196px;
    top: 50px;
    width: 806px;
    height: 1100px;
    background: var(--sign-black);
    color: var(--sign-white);
    font-family: "Bebas Neue", "Arial Narrow", sans-serif;
    font-weight: 400;
  }
  .motel-name {
    position: absolute;
    left: 132px;
    top: 262px;
    margin: 0;
    display: flex;
    flex-direction: column;
    align-items: flex-start;
    font-weight: 400;
    line-height: 1;
    white-space: nowrap;
  }
  .motel-name span {
    display: block;
  }
  .motel-name-the {
    font-size: 140px;
    letter-spacing: 1px;
  }
  .motel-name-place {
    margin-top: 4px;
    font-size: 150px;
    letter-spacing: 1px;
  }
  .motel-name-kind {
    align-self: flex-end;
    margin-top: 10px;
    font-size: 90px;
    letter-spacing: 14px;
    margin-right: -14px;
  }
  .restaurant-line {
    position: absolute;
    left: 0;
    right: 0;
    top: 770px;
    margin: 0;
    text-align: center;
    font-size: 54px;
    line-height: 1;
    letter-spacing: 0.5px;
    white-space: nowrap;
  }
</style>
</head>
<body>
  <main class="canvas">
    <section class="light-box" aria-label="The Harborvale Motel light box sign">
      <h1 class="motel-name">
        <span class="motel-name-the">The</span>
        <span class="motel-name-place">Harborvale</span>
        <span class="motel-name-kind">Motel</span>
      </h1>
      <p class="restaurant-line">Mirokawa Robatayaki Restaurant</p>
    </section>
  </main>
</body>
</html>
```